Business Card & Full Stationary design For Summit Quarry
Summit Quarry For Marble & Granite
Business Card & Full Stationary design For Summit Quarry  - Construction
Creative Brief
Professional
Eng. Karim Haddouri
C.E.O
14 Shari' Nakhil el Wadi, Rawdatein, Giza, 12487, Egypt
kbh@summitquarry.com.eg
www.summitquarry.com.eg
we need everything to be included in the design ( CD, CD Cover, Letterhead, Envelopes, portfolio cover, etc..)
q7rimo q7rimo
I would highly appreciate if you can provide your concepts showing all the required stationaries including the back side of the B.Card ( Letterhead, 2 size envelope, Portfolio cover, CD, CD cover, Backgrounds for smartphones and Computers .)
Vonto Vonto

```html
<!DOCTYPE html>
<html lang="en">
<head>
<meta charset="utf-8">
<title>Summit Quarry – Business Card</title>
<link href="https://fonts.googleapis.com/css2?family=Open+Sans:wght@300;400;600&display=swap" rel="stylesheet">
<style>
  :root {
    --backdrop: #ececec;
    --card-white: #ffffff;
    --stone-grey: #6e6a69;
    --sand: #cfc5ae;
    --gold-text: #c9bd9c;
    --ink: #4a4747;
    --ink-soft: #6d6a6a;
  }
  * { box-sizing: border-box; margin: 0; padding: 0; }
  html, body {
    width: 1200px; height: 939px; overflow: hidden;
    background: var(--backdrop);
    font-family: "Open Sans", Arial, sans-serif;
  }
  .stationery {
    position: relative; width: 1200px; height: 939px;
    display: flex; align-items: center; justify-content: center; gap: 60px;
  }
  .card {
    position: relative; width: 520px; height: 300px; overflow: hidden;
    box-shadow: 0 6px 18px rgba(0,0,0,0.12);
  }
  .card-front { background: var(--card-white); }
  .card-back {
    background: var(--stone-grey);
    display: flex; align-items: center; justify-content: center;
  }
  .corner-curve { position: absolute; inset: 0; width: 100%; height: 100%; }
  .brand-name {
    font-weight: 300; letter-spacing: 1px; color: var(--gold-text);
  }
  .card-front .brand-name {
    position: absolute; top: 44px; left: 200px; font-size: 34px;
  }
  .card-back .brand-name { font-size: 40px; color: var(--gold-text); }
  .holder { position: absolute; left: 36px; top: 128px; }
  .holder-name { font-size: 17px; font-weight: 400; color: var(--ink); }
  .holder-title { font-size: 15px; font-weight: 400; color: var(--ink); margin-top: 1px; }
  .contact-list {
    position: absolute; left: 36px; top: 188px; list-style: none;
    font-size: 9.5px; line-height: 15px; color: var(--ink-soft);
  }
  .contact-list li { display: flex; align-items: center; gap: 6px; }
  .contact-list svg { width: 9px; height: 9px; flex: none; }
</style>
</head>
<body>
<main class="stationery">
  <section class="card card-front" aria-label="Business card front">
    <svg class="corner-curve" viewBox="0 0 520 300" aria-hidden="true">
      <path d="M520 90 L520 300 L270 300 C330 260 440 190 520 90 Z" fill="var(--sand)"/>
      <path d="M250 300 C320 255 430 175 490 70 L520 80 C450 180 345 260 290 300 Z" fill="var(--stone-grey)"/>
    </svg>
    <div class="brand-name">Summit Quarry</div>
    <div class="holder">
      <p class="holder-name">Karim Haddouri</p>
      <p class="holder-title">Consultant</p>
    </div>
    <ul class="contact-list">
      <li><svg viewBox="0 0 10 10"><path d="M5 0.5a3 3 0 0 1 3 3c0 2.2-3 6-3 6s-3-3.8-3-6a3 3 0 0 1 3-3z" fill="var(--ink-soft)"/></svg>14 Shari' Nakhil el Wadi, Rawdatein, Giza, 12487</li>
      <li><svg viewBox="0 0 10 10"><path d="M2 0.8l2 2-1 1.2a6 6 0 0 0 3 3l1.2-1 2 2-1.4 1.4C4.5 9 1 5.5 0.6 2.2z" fill="var(--ink-soft)"/></svg>T. 010 482 3915</li>
      <li><svg viewBox="0 0 10 10"><rect x="0.5" y="2" width="9" height="6" fill="none" stroke="var(--ink-soft)"/><path d="M0.5 2l4.5 3.5L9.5 2" fill="none" stroke="var(--ink-soft)"/></svg>kbh@summitquarry.com.eg</li>
      <li><svg viewBox="0 0 10 10"><path d="M2 0.8l2 2-1 1.2a6 6 0 0 0 3 3l1.2-1 2 2-1.4 1.4C4.5 9 1 5.5 0.6 2.2z" fill="var(--ink-soft)"/></svg>M. 010 482 3916</li>
      <li><svg viewBox="0 0 10 10"><circle cx="5" cy="5" r="4.3" fill="none" stroke="var(--ink-soft)"/><path d="M0.7 5h8.6M5 0.7c-2.4 2.4-2.4 6.2 0 8.6M5 0.7c2.4 2.4 2.4 6.2 0 8.6" fill="none" stroke="var(--ink-soft)" stroke-width="0.7"/></svg>www.summitquarry.com.eg</li>
    </ul>
  </section>

  <section class="card card-back" aria-label="Business card back">
    <div class="brand-name">Summit Quarry</div>
  </section>
</main>
</body>
</html>
```